Tarnwick Bathrooms

Fix our flyer add as the one we got made has the wrong phone number on it would like different photos on it

Want it to Stand out and be in your face!

I will attach our logo
phone number is 0487652970
Email is Jory@tarnwickbathrooms.com.au

happy to keep all prices the same

If you can make it better happy to tip $$

```html
<!DOCTYPE html>
<html lang="en">
<head>
<meta charset="UTF-8">
<title>Tarnwick Bathrooms Flyer</title>
<link href="https://fonts.googleapis.com/css2?family=Montserrat:wght@600;700;800&family=Poppins:ital,wght@0,600;0,700;0,800;1,400&family=Barlow:wght@500;600&family=Mukta:wght@500&display=swap" rel="stylesheet">
<style>
  :root {
    --blue: #1466b6;
    --blue-bright: #1a7ad2;
    --navy: #0d3e78;
    --charcoal: #29292b;
    --ink: #2b2b2d;
    --light: #f2f2f2;
    --light-gray: #d4d4d6;
    --white: #ffffff;
    --stage: #333335;
  }
  * { margin: 0; padding: 0; box-sizing: border-box; }
  html, body {
    width: 1011px; height: 1200px; overflow: hidden;
    background: var(--stage);
  }
  .flyer-frame {
    position: absolute; left: 81px; top: 0;
    width: 849px; height: 1200px; overflow: hidden;
  }
  .flyer {
    position: absolute; left: 0; top: 0;
    width: 1201px; height: 1698px;
    transform: scale(0.7067); transform-origin: top left;
    background: var(--white);
    font-family: "Montserrat", sans-serif;
  }
  .abs { position: absolute; }

  /* header */
  .logo-box {
    left: 0; top: 0; width: 368px; height: 235px; background: var(--white);
    display: flex; align-items: center; justify-content: center;
  }
  .brand-name {
    font-family: "Montserrat", sans-serif; font-weight: 700;
    color: var(--blue); font-size: 38px; line-height: 1.1;
    text-align: center; text-transform: uppercase; letter-spacing: 1px;
  }
  .hero-photo {
    left: 368px; top: 0; width: 833px; height: 583px;
    background: linear-gradient(120deg, #d9cfc2 0%, #efe9e1 35%, #c9b79c 60%, #e8e2da 80%, #8d8a86 100%);
  }
  .header-shapes { left: 0; top: 0; width: 1201px; height: 583px; }
  .headline-panel { left: 56px; top: 270px; color: var(--white); }
  .headline-kicker {
    font-weight: 800; font-size: 33px; letter-spacing: 0.5px; margin-bottom: 10px;
  }
  .headline-main {
    font-weight: 800; font-size: 78px; line-height: 82px; letter-spacing: 0.5px;
  }

  .region-band {
    left: 0; top: 583px; width: 1201px; height: 93px; background: var(--charcoal);
    color: var(--white); font-weight: 700; font-size: 45px;
    padding-left: 56px; line-height: 93px; letter-spacing: 0; white-space: nowrap;
  }

  /* services */
  .services-area {
    left: 0; top: 676px; width: 1201px; height: 794px;
    background: linear-gradient(135deg, #ededed 0%, #f8f8f8 40%, #efefef 100%);
  }
  .lower-shapes { left: 0; top: 0; width: 1201px; height: 1698px; }
  .tagline { left: 56px; top: 700px; }
  .tagline-title {
    font-family: "Poppins", sans-serif; font-weight: 800; font-size: 68px;
    color: var(--ink); line-height: 80px; letter-spacing: -1px;
  }
  .tagline-sub {
    font-family: "Mukta", sans-serif; font-weight: 500; font-size: 64px;
    color: var(--blue); line-height: 66px; white-space: nowrap;
  }
  .service {
    display: flex; align-items: center; gap: 10px;
    font-family: "Barlow", sans-serif; font-weight: 500; font-size: 35px; color: var(--ink);
    white-space: nowrap;
  }
  .service svg { width: 36px; height: 38px; flex: none; }

  /* packages */
  .package {
    width: 321px; height: 343px; top: 1014px; border-radius: 22px; overflow: hidden;
    background: var(--light); box-shadow: 0 6px 16px rgba(0,0,0,0.22);
  }
  .package-photo { width: 100%; height: 208px; }
  .photo-bathroom { background: linear-gradient(135deg, #1f4a37 0%, #3a6b4f 45%, #d9d9d6 75%, #7b6552 100%); }
  .photo-ensuite { background: linear-gradient(90deg, #1e1e20 0%, #c9ced3 35%, #e8ecef 55%, #8e5a36 80%, #b98458 100%); }
  .photo-laundry { background: linear-gradient(120deg, #8e7f77 0%, #a9998f 40%, #d8cfc4 65%, #3a3a3c 100%); }
  .save-badge {
    position: absolute; left: 50%; top: 170px; transform: translateX(-50%);
    width: 76px; height: 76px; border-radius: 50%;
    background: var(--charcoal); border: 3px solid var(--white);
    display: flex; flex-direction: column; align-items: center; justify-content: center;
    color: var(--white); font-family: "Poppins", sans-serif; line-height: 1;
  }
  .save-word { font-weight: 700; font-size: 15px; }
  .save-upto { font-weight: 600; font-size: 6px; margin: 2px 0; }
  .save-amount { font-family: "Barlow", sans-serif; font-weight: 600; font-size: 16px; color: #3fa2ff; }
  .package-name {
    position: absolute; left: 0; top: 248px; width: 100%; text-align: center;
    font-family: "Poppins", sans-serif; font-weight: 700; font-size: 20px; color: var(--ink);
  }
  .price-bar {
    position: absolute; left: 0; bottom: 0; width: 100%; height: 57px;
    background: var(--blue-bright); color: var(--white);
    display: flex; align-items: center; justify-content: center; gap: 8px;
    font-family: "Poppins", sans-serif;
  }
  .price-label { font-weight: 600; font-size: 13px; }
  .price-value { font-weight: 800; font-size: 44px; letter-spacing: -0.5px; }

  .terms {
    left: 68px; top: 1402px; font-family: "Poppins", sans-serif; font-style: italic;
    font-weight: 400; font-size: 12px; color: var(--ink);
  }
  .fixtures-note {
    left: 545px; top: 1388px; font-family: "Barlow", sans-serif; font-weight: 500;
    font-size: 31px; color: var(--white); white-space: nowrap;
  }

  /* contact */
  .phone-icon {
    left: 56px; top: 1505px; width: 85px; height: 85px; border-radius: 10px;
    background: var(--charcoal);
  }
  .contact-label {
    left: 158px; top: 1506px; font-family: "Poppins", sans-serif; font-weight: 700;
    font-size: 26px; color: var(--white); letter-spacing: 0.3px;
  }
  .contact-phone {
    left: 150px; top: 1534px; font-family: "Poppins", sans-serif; font-weight: 800;
    font-size: 58px; color: var(--white); letter-spacing: 1px; white-space: nowrap;
  }
  .globe-icon { left: 692px; top: 1558px; width: 52px; height: 52px; }
  .web-details {
    left: 755px; top: 1556px; font-family: "Montserrat", sans-serif; font-weight: 600;
    font-size: 21px; line-height: 31px; color: var(--white); letter-spacing: 0.8px;
  }
</style>
</head>
<body>
<div class="flyer-frame">
  <div class="flyer">
    <!-- header -->
    <div class="abs hero-photo" role="img" aria-label="Photo of a bright renovated bathroom with stone vanity, vessel basin and arched mirror"></div>
    <div class="abs logo-box"><div class="brand-name">Tarnwick<br>Bathrooms</div></div>
    <svg class="abs header-shapes" viewBox="0 0 1201 583" aria-hidden="true">
      <polygon points="368,150 532,235 368,235" fill="var(--navy)"/>
      <rect x="0" y="235" width="532" height="348" fill="var(--blue)"/>
    </svg>
    <div class="abs headline-panel">
      <div class="headline-kicker">TARNWICK BATHROOMS</div>
      <div class="headline-main">FULLY<br>LICENSED<br>&amp; INSURED</div>
    </div>
    <div class="abs region-band">ILLAWARRA BASED AND FAMILY OPERATED</div>

    <!-- services -->
    <div class="abs services-area"></div>
    <svg class="abs lower-shapes" viewBox="0 0 1201 1698" aria-hidden="true">
      <polygon points="400,1165 1201,1165 1201,1210 400,1210" fill="var(--light-gray)"/>
      <polygon points="420,1232 1201,1232 1201,1640 0,1640 0,1470 395,1470 532,1357 420,1357" fill="var(--blue)"/>
      <polygon points="0,1463 388,1463 527,1350 534,1356 396,1471 0,1471" fill="var(--light-gray)"/>
      <polygon points="690,1467 1201,1467 1201,1645 520,1645" fill="var(--light-gray)"/>
      <polygon points="705,1497 1201,1497 1201,1645 545,1645" fill="var(--white)"/>
      <polygon points="708,1517 1201,1517 1201,1645 575,1645" fill="var(--charcoal)"/>
      <rect x="0" y="1635" width="560" height="10" fill="var(--light-gray)"/>
    </svg>

    <div class="abs tagline">
      <div class="tagline-title">BUILT TO LAST</div>
      <div class="tagline-sub">Your local renovation specialist</div>
    </div>

    <svg width="0" height="0" style="position:absolute">
      <symbol id="tick-box" viewBox="0 0 36 38">
        <rect x="2" y="8" width="26" height="26" fill="none" stroke="#2b2b2d" stroke-width="2.5"/>
        <polyline points="8,20 15,29 32,3" fill="none" stroke="#1466b6" stroke-width="4" stroke-linecap="round" stroke-linejoin="round"/>
      </symbol>
    </svg>
    <div class="abs service" style="left:56px;top:858px"><svg><use href="#tick-box"/></svg>Demolition</div>
    <div class="abs service" style="left:312px;top:858px"><svg><use href="#tick-box"/></svg>Electrical</div>
    <div class="abs service" style="left:545px;top:858px"><svg><use href="#tick-box"/></svg>Carpentry</div>
    <div class="abs service" style="left:777px;top:858px"><svg><use href="#tick-box"/></svg>Design Consultation</div>
    <div class="abs service" style="left:56px;top:933px"><svg><use href="#tick-box"/></svg>Waterproofing</div>
    <div class="abs service" style="left:357px;top:933px"><svg><use href="#tick-box"/></svg>Plumbing</div>
    <div class="abs service" style="left:577px;top:933px"><svg><use href="#tick-box"/></svg>Tiling</div>

    <!-- packages -->
    <div class="abs package" style="left:90px">
      <div class="package-photo photo-bathroom" role="img" aria-label="Photo of a main bathroom vanity with basin and green tiled wall"></div>
      <div class="save-badge"><span class="save-word">SAVE</span><span class="save-upto">UP TO</span><span class="save-amount">$4,000</span></div>
      <div class="package-name">MAIN BATHROOM PACKAGE</div>
      <div class="price-bar"><span class="price-label">Price Starts From</span><span class="price-value">$18,900</span></div>
    </div>
    <div class="abs package" style="left:446px">
      <div class="package-photo photo-ensuite" role="img" aria-label="Photo of an ensuite with freestanding bath and city window view"></div>
      <div class="save-badge"><span class="save-word">SAVE</span><span class="save-upto">UP TO</span><span class="save-amount">$4,000</span></div>
      <div class="package-name">ENSUITE PACKAGE</div>
      <div class="price-bar"><span class="price-label">Price Starts From</span><span class="price-value">$14,900</span></div>
    </div>
    <div class="abs package" style="left:801px">
      <div class="package-photo photo-laundry" role="img" aria-label="Photo of a laundry with front loading washer under a stone benchtop"></div>
      <div class="save-badge"><span class="save-word">SAVE</span><span class="save-upto">UP TO</span><span class="save-amount">$4,000</span></div>
      <div class="package-name">LAUNDRY PACKAGE</div>
      <div class="price-bar"><span class="price-label">Price Starts From</span><span class="price-value">$9,900</span></div>
    </div>

    <div class="abs terms">*Terms and conditions apply and onsite quote required.</div>
    <div class="abs fixtures-note">Organisation And Delivery Of All Fixtures</div>

    <!-- contact -->
    <div class="abs phone-icon">
      <svg viewBox="0 0 85 85" width="85" height="85" aria-hidden="true">
        <path d="M22 18c3-2 6-2 8 1l6 10c1 2 1 5-1 6l-4 3c2 6 8 13 14 16l3-4c2-2 4-2 6-1l10 6c3 2 3 5 1 8l-4 5c-3 3-8 3-13 1C34 64 22 52 17 38c-2-5-1-10 1-13z" fill="#fff"/>
        <path d="M50 22a14 14 0 0 1 13 13M50 14a22 22 0 0 1 21 21" fill="none" stroke="#fff" stroke-width="3.5" stroke-linecap="round"/>
      </svg>
    </div>
    <div class="abs contact-label">GET IN TOUCH WITH US</div>
    <div class="abs contact-phone">0487 652 970</div>

    <svg class="abs globe-icon" viewBox="0 0 52 52" aria-hidden="true">
      <g fill="none" stroke="#fff" stroke-width="3">
        <circle cx="26" cy="26" r="22"/>
        <ellipse cx="26" cy="26" rx="10" ry="22"/>
        <line x1="4" y1="26" x2="48" y2="26"/>
        <path d="M8 15h36M8 37h36"/>
      </g>
    </svg>
    <div class="abs web-details">www.tarnwickbathrooms.com.au<br>jory@tarnwickbathrooms.com.au</div>
  </div>
</div>
</body>
</html>
```